Need a Shopvarnel Design for a new company called DeskRaven

DeskRaven is a new US company that sells compatible toner cartridges and remanufactured ink jet cartridges and other office supplies direct from the manufacturers. We will need to add an app like Gear Locator to the site so that users can search for supplies for their machine model. We need to connect our Quorvex and tilmo inventory with the ShopVarnel site through Syncpyle.

```html
<!DOCTYPE html>
<html lang="en">
<head>
<meta charset="utf-8">
<title>DeskRaven – Premium Office Supplies</title>
<link rel="stylesheet" href="https://fonts.googleapis.com/css2?family=Quicksand:wght@500;600;700&family=Arimo:wght@400;700&family=Poppins:wght@500;600&display=swap">
<style>
:root{
  --ink:#1e1e1e;
  --text:#333;
  --muted:#666;
  --line:#ddd;
  --cyan:#0aabe6;
  --magenta:#ec008c;
  --yellow:#fff200;
  --price:#e5097f;
  --star:#f7a600;
  --white:#fff;
}
*{box-sizing:border-box;margin:0;padding:0}
html,body{width:1200px;height:2875px;overflow:hidden;background:var(--white)}
body{position:relative;font-family:Arimo,Arial,sans-serif;color:var(--text)}
.abs{position:absolute}
ul{list-style:none}

/* utility bar */
.utility-bar{left:0;top:0;width:1200px;height:52px;background:var(--ink);color:var(--white);font:500 12px Poppins,sans-serif;letter-spacing:.3px}
.utility-bar .trial{position:absolute;left:111px;top:19px}
.utility-links{position:absolute;right:111px;top:19px;display:flex;gap:26px}
.utility-links span{display:flex;align-items:center;gap:7px}
.utility-links svg{width:12px;height:12px;fill:var(--white)}

/* header */
.social{left:111px;top:104px;display:flex;gap:6px}
.social span{width:33px;height:33px;border:2px solid #555;border-radius:50%}
.brand{left:450px;top:95px;height:56px;display:flex;align-items:center;gap:12px}
.brand .dot{width:56px;height:56px;border-radius:50%;background:var(--ink)}
.brand .name{font:700 34px Quicksand,sans-serif;color:var(--ink)}
.search{left:842px;top:101px;width:246px;height:42px;border:1px solid #ccc;font-size:14px;color:#555;padding:12px 15px}
.search svg{position:absolute;right:14px;top:13px;width:14px;height:14px}

/* navigation */
.main-nav{left:111px;top:186px;width:977px;height:61px;background:var(--cyan);display:flex;align-items:center;justify-content:space-around;padding:0 40px;font:500 16px Poppins,sans-serif;color:var(--white)}

/* finder */
.finder{left:111px;top:257px;width:264px;height:440px;border:1px solid #e5e5e5;box-shadow:0 1px 4px rgba(0,0,0,.12)}
.finder h2{height:54px;background:var(--ink);color:var(--white);font:600 17px Poppins,sans-serif;text-align:center;line-height:54px}
.finder ul{padding:27px 13px 0}
.finder li{height:43px;border:1px solid #ccc;margin-bottom:12.5px;font-size:14.5px;color:#555;padding:12px 15px;position:relative}
.finder li::after{content:"";position:absolute;right:12px;top:19px;border:5px solid transparent;border-top-color:#555}

.hero{left:383px;top:257px;width:706px;height:440px;background:linear-gradient(135deg,#555,#3a3a3a 55%,#2a2a2a);color:var(--white);text-align:center;font-family:Quicksand,sans-serif}
.hero .title{position:absolute;left:0;right:0;top:127px;font-size:70px;font-weight:500}
.hero .sub{position:absolute;left:0;right:0;top:214px;font-size:31px;font-weight:700}
.hero .sub2{position:absolute;left:0;right:0;top:260px;font-size:26px;font-weight:700}

/* section headings */
.section-title{left:0;width:1200px;text-align:center;font:600 35px Quicksand,sans-serif;color:var(--ink)}
.section-title::after{content:"";display:block;width:46px;height:3px;background:var(--cyan);margin:13px auto 0}

/* categories */
.category{top:843px;width:314px;height:310px}
.category .photo{height:245px}
.category .label{height:65px;line-height:65px;text-align:center;font:600 23px Quicksand,sans-serif;color:var(--white)}

/* product cards */
.product{width:235px;height:288px;border:1px solid #eee;box-shadow:0 1px 4px rgba(0,0,0,.1);text-align:center;font-family:Quicksand,sans-serif}
.product .photo{margin:30px auto 0;width:200px;height:145px;border-radius:4px}
.product .stars{margin-top:12px;display:flex;justify-content:center;gap:3px}
.product .stars svg{width:13px;height:13px;fill:var(--star)}
.product .name{margin-top:6px;font-size:20px;font-weight:500;color:#444}
.product .price{margin-top:7px;font-size:19px;font-weight:600;color:var(--price)}

/* promo */
.promo{left:111px;top:2123px;width:978px;height:355px;background:linear-gradient(100deg,#e8d630 0%,#d3307a 22%,#2b8fd1 40%,#4e5966 62%,#4d5864 100%);color:var(--white);font-family:Quicksand,sans-serif;text-align:center}
.promo .copy{position:absolute;left:530px;width:440px;top:72px}
.promo h3{font-size:46px;font-weight:700;white-space:nowrap}
.promo .deal{font-size:66px;font-weight:700;color:var(--yellow);margin-top:2px}
.promo .cta{display:inline-block;margin-top:14px;border:2px solid var(--white);padding:11px 25px;font:600 21px Poppins,sans-serif}

/* footer */
.site-footer{left:0;top:2536px;width:1200px;height:339px;background:var(--ink);color:var(--white)}
.col{position:absolute;top:57px}
.col h4{font:500 15.5px Poppins,sans-serif;letter-spacing:.3px}
.col ul{margin-top:26px}
.col li{font-size:13px;height:25.6px;padding-left:27px;position:relative}
.col li::before{content:"";position:absolute;left:3px;top:4px;border:4px solid transparent;border-left:5px solid var(--white)}
.stores li{padding-left:29px;font-size:11.5px;height:28.5px}
.stores li::before{display:none}
.stores svg{position:absolute;left:1px;top:0;width:13px;height:13px;fill:var(--white)}
.stores a{color:var(--white)}
.newsletter p{font-size:11.5px;line-height:15px;margin-top:26px;width:170px}
.newsletter .field{margin-top:14px;width:161px;height:39px;background:var(--white);position:relative;color:#777;font-size:11px;padding:13px 15px}
.newsletter .field span{position:absolute;right:0;top:0;width:35px;height:39px;background:var(--cyan)}
.newsletter .field svg{position:absolute;right:11px;top:13px;width:13px;height:13px;fill:var(--white)}
.copyright{position:absolute;left:0;right:0;top:267px;border-top:1px solid #333;padding-top:26px;text-align:center;font-size:13px}
</style>
</head>
<body>

<header>
  <div class="abs utility-bar">
    <span class="trial">FREE 7 DAY TRIAL!</span>
    <div class="utility-links">
      <span><svg viewBox="0 0 12 12"><rect x="1" y="5" width="10" height="7"/><rect x="0" y="3" width="12" height="2"/></svg>QUESTIONS? CONTACT US</span>
      <span><svg viewBox="0 0 12 12"><circle cx="6" cy="3.5" r="3"/><path d="M0 12c0-4 3-5 6-5s6 1 6 5z"/></svg>SIGN IN OR REGISTER</span>
      <span><svg viewBox="0 0 12 12"><path d="M6 11L1 6a3 3 0 015-4 3 3 0 015 4z"/></svg>FAVORITES</span>
      <span><svg viewBox="0 0 12 12"><path d="M0 1h2l2 7h7l1-5H3"/><circle cx="5" cy="10.5" r="1.2"/><circle cx="10" cy="10.5" r="1.2"/></svg>CART 0</span>
    </div>
  </div>

  <div class="abs social"><span></span><span></span><span></span><span></span><span></span></div>

  <div class="abs brand">
    <span class="dot"></span>
    <span class="name">DeskRaven</span>
  </div>

  <div class="abs search">Search the store
    <svg viewBox="0 0 14 14" fill="none" stroke="#333" stroke-width="2"><circle cx="6" cy="6" r="4.5"/><path d="M9.5 9.5L13 13"/></svg>
  </div>

  <nav class="abs main-nav"><span>HOME</span><span>TONERS</span><span>INKS</span><span>OFFICE PRODUCTS</span><span>RECYCLE</span><span>ABOUT US</span></nav>
</header>

<main>
  <aside class="abs finder">
    <h2>FIND YOUR PART</h2>
    <ul>
      <li>Choose Your Year</li><li>Choose Your Make</li><li>Choose Your Model</li>
      <li>Choose Your Brand</li><li>Choose Your Color</li><li>Choose Your Price</li>
    </ul>
  </aside>

  <section class="abs hero" role="img" aria-label="Close-up photo of a printer carriage with colour ink cartridges">
    <div class="title">DeskRaven</div>
    <div class="sub">Premium Office Supplies for a Steal...</div>
    <div class="sub2">Quick Shipping &amp; 100% guarantee</div>
  </section>

  <h2 class="abs section-title" style="top:748px">Featured Categories</h2>
  <div class="abs category" style="left:111px">
    <div class="photo" role="img" aria-label="Photo of colour toner cartridges on a wooden table" style="background:linear-gradient(135deg,#c9c23a,#c8407a 45%,#2a8ed0 70%,#444)"></div>
    <div class="label" style="background:var(--cyan)">Toner Cartridges</div>
  </div>
  <div class="abs category" style="left:443px">
    <div class="photo" role="img" aria-label="Photo of black and colour inkjet cartridges in a printer" style="background:linear-gradient(160deg,#5f7686,#2f3c46 60%,#1f272d)"></div>
    <div class="label" style="background:var(--magenta)">Inkjet Cartridges</div>
  </div>
  <div class="abs category" style="left:775px">
    <div class="photo" role="img" aria-label="Photo of a row of ink cartridges in a printer" style="background:linear-gradient(160deg,#3c3c3c,#6a6a6a 50%,#bfbfbf)"></div>
    <div class="label" style="background:var(--yellow);color:#444">Other</div>
  </div>

  <h2 class="abs section-title" style="top:1229px">Featured Products</h2>
  <article class="abs product" style="left:111px;top:1325px"><div class="photo" role="img" aria-label="Product photo of four toner cartridges" style="background:linear-gradient(90deg,#3aa0c8,#c44a90,#d8c838,#444)"></div><div class="stars"><svg viewBox="0 0 10 10"><path d="M5 0l1.5 3.3 3.5.3-2.7 2.3.9 3.5L5 7.6 1.8 9.4l.9-3.5L0 3.6l3.5-.3z"/></svg><svg viewBox="0 0 10 10"><path d="M5 0l1.5 3.3 3.5.3-2.7 2.3.9 3.5L5 7.6 1.8 9.4l.9-3.5L0 3.6l3.5-.3z"/></svg><svg viewBox="0 0 10 10"><path d="M5 0l1.5 3.3 3.5.3-2.7 2.3.9 3.5L5 7.6 1.8 9.4l.9-3.5L0 3.6l3.5-.3z"/></svg><svg viewBox="0 0 10 10"><path d="M5 0l1.5 3.3 3.5.3-2.7 2.3.9 3.5L5 7.6 1.8 9.4l.9-3.5L0 3.6l3.5-.3z"/></svg><svg viewBox="0 0 10 10"><path d="M5 0l1.5 3.3 3.5.3-2.7 2.3.9 3.5L5 7.6 1.8 9.4l.9-3.5L0 3.6l3.5-.3z"/></svg></div><div class="name">Product Name</div><div class="price">£30.00</div></article>
  <article class="abs product" style="left:359px;top:1325px"><div class="photo" role="img" aria-label="Product photo of black toner cartridges with colour tabs" style="background:linear-gradient(90deg,#2a2a2a,#3a3a3a 60%,#e4d93a)"></div><div class="stars"><svg viewBox="0 0 10 10"><path d="M5 0l1.5 3.3 3.5.3-2.7 2.3.9 3.5L5 7.6 1.8 9.4l.9-3.5L0 3.6l3.5-.3z"/></svg><svg viewBox="0 0 10 10"><path d="M5 0l1.5 3.3 3.5.3-2.7 2.3.9 3.5L5 7.6 1.8 9.4l.9-3.5L0 3.6l3.5-.3z"/></svg><svg viewBox="0 0 10 10"><path d="M5 0l1.5 3.3 3.5.3-2.7 2.3.9 3.5L5 7.6 1.8 9.4l.9-3.5L0 3.6l3.5-.3z"/></svg><svg viewBox="0 0 10 10"><path d="M5 0l1.5 3.3 3.5.3-2.7 2.3.9 3.5L5 7.6 1.8 9.4l.9-3.5L0 3.6l3.5-.3z"/></svg><svg viewBox="0 0 10 10"><path d="M5 0l1.5 3.3 3.5.3-2.7 2.3.9 3.5L5 7.6 1.8 9.4l.9-3.5L0 3.6l3.5-.3z"/></svg></div><div class="name">Product Name</div><div class="price">£30.00</div></article>
  <article class="abs product" style="left:606px;top:1325px"><div class="photo" role="img" aria-label="Product photo of stacked toner cartridges" style="background:linear-gradient(180deg,#d84a8e,#2c2c2c 30%,#d3c93a 55%,#2c2c2c 70%,#35a6d3)"></div><div class="stars"><svg viewBox="0 0 10 10"><path d="M5 0l1.5 3.3 3.5.3-2.7 2.3.9 3.5L5 7.6 1.8 9.4l.9-3.5L0 3.6l3.5-.3z"/></svg><svg viewBox="0 0 10 10"><path d="M5 0l1.5 3.3 3.5.3-2.7 2.3.9 3.5L5 7.6 1.8 9.4l.9-3.5L0 3.6l3.5-.3z"/></svg><svg viewBox="0 0 10 10"><path d="M5 0l1.5 3.3 3.5.3-2.7 2.3.9 3.5L5 7.6 1.8 9.4l.9-3.5L0 3.6l3.5-.3z"/></svg><svg viewBox="0 0 10 10"><path d="M5 0l1.5 3.3 3.5.3-2.7 2.3.9 3.5L5 7.6 1.8 9.4l.9-3.5L0 3.6l3.5-.3z"/></svg><svg viewBox="0 0 10 10"><path d="M5 0l1.5 3.3 3.5.3-2.7 2.3.9 3.5L5 7.6 1.8 9.4l.9-3.5L0 3.6l3.5-.3z"/></svg></div><div class="name">Product Name</div><div class="price">£30.00</div></article>
  <article class="abs product" style="left:853px;top:1325px"><div class="photo" role="img" aria-label="Product photo of a magenta toner cartridge" style="background:linear-gradient(160deg,#2c2c2c,#d4487e 50%,#e07a3a)"></div><div class="stars"><svg viewBox="0 0 10 10"><path d="M5 0l1.5 3.3 3.5.3-2.7 2.3.9 3.5L5 7.6 1.8 9.4l.9-3.5L0 3.6l3.5-.3z"/></svg><svg viewBox="0 0 10 10"><path d="M5 0l1.5 3.3 3.5.3-2.7 2.3.9 3.5L5 7.6 1.8 9.4l.9-3.5L0 3.6l3.5-.3z"/></svg><svg viewBox="0 0 10 10"><path d="M5 0l1.5 3.3 3.5.3-2.7 2.3.9 3.5L5 7.6 1.8 9.4l.9-3.5L0 3.6l3.5-.3z"/></svg><svg viewBox="0 0 10 10"><path d="M5 0l1.5 3.3 3.5.3-2.7 2.3.9 3.5L5 7.6 1.8 9.4l.9-3.5L0 3.6l3.5-.3z"/></svg><svg viewBox="0 0 10 10"><path d="M5 0l1.5 3.3 3.5.3-2.7 2.3.9 3.5L5 7.6 1.8 9.4l.9-3.5L0 3.6l3.5-.3z"/></svg></div><div class="name">Product Name</div><div class="price">£30.00</div></article>

  <h2 class="abs section-title" style="top:1678px">New Products</h2>
  <article class="abs product" style="left:111px;top:1773px"><div class="photo" role="img" aria-label="Product photo of four ink cartridges in a row" style="background:linear-gradient(90deg,#4a9fd0,#c84a6a,#e0c83a,#333)"></div><div class="stars"><svg viewBox="0 0 10 10"><path d="M5 0l1.5 3.3 3.5.3-2.7 2.3.9 3.5L5 7.6 1.8 9.4l.9-3.5L0 3.6l3.5-.3z"/></svg><svg viewBox="0 0 10 10"><path d="M5 0l1.5 3.3 3.5.3-2.7 2.3.9 3.5L5 7.6 1.8 9.4l.9-3.5L0 3.6l3.5-.3z"/></svg><svg viewBox="0 0 10 10"><path d="M5 0l1.5 3.3 3.5.3-2.7 2.3.9 3.5L5 7.6 1.8 9.4l.9-3.5L0 3.6l3.5-.3z"/></svg><svg viewBox="0 0 10 10"><path d="M5 0l1.5 3.3 3.5.3-2.7 2.3.9 3.5L5 7.6 1.8 9.4l.9-3.5L0 3.6l3.5-.3z"/></svg><svg viewBox="0 0 10 10"><path d="M5 0l1.5 3.3 3.5.3-2.7 2.3.9 3.5L5 7.6 1.8 9.4l.9-3.5L0 3.6l3.5-.3z"/></svg></div><div class="name">Product Name</div><div class="price">£30.00</div></article>
  <article class="abs product" style="left:359px;top:1773px"><div class="photo" role="img" aria-label="Product photo of three inkjet cartridges" style="background:linear-gradient(90deg,#e4d83a,#333 45%,#d0508e)"></div><div class="stars"><svg viewBox="0 0 10 10"><path d="M5 0l1.5 3.3 3.5.3-2.7 2.3.9 3.5L5 7.6 1.8 9.4l.9-3.5L0 3.6l3.5-.3z"/></svg><svg viewBox="0 0 10 10"><path d="M5 0l1.5 3.3 3.5.3-2.7 2.3.9 3.5L5 7.6 1.8 9.4l.9-3.5L0 3.6l3.5-.3z"/></svg><svg viewBox="0 0 10 10"><path d="M5 0l1.5 3.3 3.5.3-2.7 2.3.9 3.5L5 7.6 1.8 9.4l.9-3.5L0 3.6l3.5-.3z"/></svg><svg viewBox="0 0 10 10"><path d="M5 0l1.5 3.3 3.5.3-2.7 2.3.9 3.5L5 7.6 1.8 9.4l.9-3.5L0 3.6l3.5-.3z"/></svg><svg viewBox="0 0 10 10"><path d="M5 0l1.5 3.3 3.5.3-2.7 2.3.9 3.5L5 7.6 1.8 9.4l.9-3.5L0 3.6l3.5-.3z"/></svg></div><div class="name">Product Name</div><div class="price">£30.00</div></article>
  <article class="abs product" style="left:606px;top:1773px"><div class="photo" role="img" aria-label="Product photo of two stacked inkjet cartridges" style="background:linear-gradient(180deg,#e8d43a,#2c2c2c 45%,#b05070)"></div><div class="stars"><svg viewBox="0 0 10 10"><path d="M5 0l1.5 3.3 3.5.3-2.7 2.3.9 3.5L5 7.6 1.8 9.4l.9-3.5L0 3.6l3.5-.3z"/></svg><svg viewBox="0 0 10 10"><path d="M5 0l1.5 3.3 3.5.3-2.7 2.3.9 3.5L5 7.6 1.8 9.4l.9-3.5L0 3.6l3.5-.3z"/></svg><svg viewBox="0 0 10 10"><path d="M5 0l1.5 3.3 3.5.3-2.7 2.3.9 3.5L5 7.6 1.8 9.4l.9-3.5L0 3.6l3.5-.3z"/></svg><svg viewBox="0 0 10 10"><path d="M5 0l1.5 3.3 3.5.3-2.7 2.3.9 3.5L5 7.6 1.8 9.4l.9-3.5L0 3.6l3.5-.3z"/></svg><svg viewBox="0 0 10 10"><path d="M5 0l1.5 3.3 3.5.3-2.7 2.3.9 3.5L5 7.6 1.8 9.4l.9-3.5L0 3.6l3.5-.3z"/></svg></div><div class="name">Product Name</div><div class="price">£30.00</div></article>
  <article class="abs product" style="left:853px;top:1773px"><div class="photo" role="img" aria-label="Product photo of ink refill bottles" style="background:linear-gradient(180deg,#2a4a8a,#e0e4ea 60%,#b07058)"></div><div class="stars"><svg viewBox="0 0 10 10"><path d="M5 0l1.5 3.3 3.5.3-2.7 2.3.9 3.5L5 7.6 1.8 9.4l.9-3.5L0 3.6l3.5-.3z"/></svg><svg viewBox="0 0 10 10"><path d="M5 0l1.5 3.3 3.5.3-2.7 2.3.9 3.5L5 7.6 1.8 9.4l.9-3.5L0 3.6l3.5-.3z"/></svg><svg viewBox="0 0 10 10"><path d="M5 0l1.5 3.3 3.5.3-2.7 2.3.9 3.5L5 7.6 1.8 9.4l.9-3.5L0 3.6l3.5-.3z"/></svg><svg viewBox="0 0 10 10"><path d="M5 0l1.5 3.3 3.5.3-2.7 2.3.9 3.5L5 7.6 1.8 9.4l.9-3.5L0 3.6l3.5-.3z"/></svg><svg viewBox="0 0 10 10"><path d="M5 0l1.5 3.3 3.5.3-2.7 2.3.9 3.5L5 7.6 1.8 9.4l.9-3.5L0 3.6l3.5-.3z"/></svg></div><div class="name">Product Name</div><div class="price">£30.00</div></article>

  <section class="abs promo" role="img" aria-label="Photo of yellow, magenta and cyan toner cartridges on a grey wooden surface">
    <div class="copy">
      <h3>Toner Cartridges</h3>
      <div class="deal">50%OFF</div>
      <span class="cta">SHOP NOW</span>
    </div>
  </section>
</main>

<footer class="abs site-footer">
  <div class="col" style="left:111px"><h4>INFORMATION</h4>
    <ul><li>Shipping Policy</li><li>Refund &amp; Returns Policy</li><li>Privacy Policy</li><li>Contact Us</li><li>Sitemap</li></ul></div>
  <div class="col" style="left:322px"><h4>WHY CHOOSE US</h4>
    <ul><li>Sed ut perspiciatis</li><li>unde omnis iste</li><li>natus error sit</li><li>voluptatem</li><li>accusantium</li><li>natus error sit</li></ul></div>
  <div class="col" style="left:512px"><h4>CATEGORIES</h4>
    <ul><li>Sed ut perspiciatis</li><li>unde omnis iste</li><li>natus error sit</li><li>voluptatem</li><li>accusantium</li><li>natus error sit</li></ul></div>
  <div class="col stores" style="left:724px;top:59px"><h4>STORES</h4>
    <ul style="margin-top:26px">
      <li><svg viewBox="0 0 13 13"><path d="M1 4c0-2 11-2 11 0v1H9V4H4v1H1z"/><rect x="2" y="6" width="9" height="6"/></svg>000-555-0148 (Phone)</li>
      <li><svg viewBox="0 0 13 13"><rect x="3" y="0" width="7" height="4"/><rect x="0" y="5" width="13" height="6"/></svg>000-555-0148&nbsp;&nbsp;&nbsp;(Fax)</li>
      <li><svg viewBox="0 0 13 13"><path d="M0 2h13v9H0z M0 2l6.5 5L13 2" fill="none" stroke="#fff" stroke-width="1.3"/></svg><a>hello@deskraven-mail.com</a></li>
      <li style="line-height:14px"><svg viewBox="0 0 13 13"><path d="M6.5 0a4.5 4.5 0 014.5 4.5C11 8 6.5 13 6.5 13S2 8 2 4.5A4.5 4.5 0 016.5 0z"/><circle cx="6.5" cy="4.5" r="1.6" fill="#1e1e1e"/></svg># 244 Lorem Ipsum Dummy<br>Text Lorem</li>
    </ul></div>
  <div class="col newsletter" style="left:927px;top:59px"><h4>NEWSLETTER</h4>
    <p>Get the latest updates on new products and upcoming sales</p>
    <div class="field">Email :<span></span><svg viewBox="0 0 13 13"><path d="M0 6L13 0 9 13 6 8z"/></svg></div>
  </div>
  <div class="copyright">© Copyright 2021 DeskRaven .All Rights Reserved</div>
</footer>

</body>
</html>
```